Price Sheet for Strength and Conditioning Facility

I need a price sheet for a training facility in Albuquerque, NM. This sheet should represent your brand and look of our facility.
Why of the Copperfield Yard?
With the help of our highly skilled team of coaches and professional educators we will help you expand your strategies to develop a new you. We will teach you how and why to balance your workouts, nutrition, recovery, sleep and mental focus to become the optimal you. We incorporate an athlete centered approach, and “yes” you are an athlete. Like the great Hal Dempsey said “If you have a body, you are an athlete.” We will help you integrate a more centered approach to your health and wellness, you will be empowered to push through until you reach your goal.
Target Market(s)
Active adults and youth athletes
Industry/Entity Type
Training
Contact Information for Business Card
Gordon Pietrowski, CSCS
Mobile number: 505-481-2267
Office: 505-372-8846
Font styles to use
Colors
Designer to choose colors to be used in the design.
Requirements
Must have
- Simple layout
- Ranch style theme
- broken into categories of services
- Use color and type font sheet
- NO TABLE! please make the table more pleasing to the eye.
Nice to have
- 8 1/2 x 11 inch sheet. Variable depending on design
- Business address: 3418 Juniper Way NE Ste. B
- Albuquerque, NM 87142
- www.thecopperfieldyard.example
- 505-372-8846

```html
<!DOCTYPE html>
<html lang="en">
<head>
<meta charset="utf-8">
<title>Copperfield Yard – Price Sheet</title>
<link rel="stylesheet" href="https://fonts.googleapis.com/css2?family=Rye&family=Anton&family=Oswald:wght@600&family=Arimo:wght@400;700&family=Bungee&display=swap">
<style>
  :root{
    --wood:#8b4a2c;
    --wood-dark:#6e3520;
    --paper-light:#f4e6c4;
    --paper-mid:#ead2a0;
    --paper-edge:#c99a5e;
    --ink:#2b2622;
    --rust:#d8452a;
    --rust-dark:#3a1a10;
    --navy:#1f3b70;
    --head-row:#d6dbe3;
    --green:#a9cf90;
    --peach:#e7ae88;
    --rule:#2a2a2a;
  }
  *{box-sizing:border-box;margin:0;padding:0}
  html,body{width:873px;height:1200px;overflow:hidden;background:var(--wood)}
  .sheet{position:relative;width:873px;height:1200px;background:linear-gradient(180deg,var(--wood) 0%,var(--wood-dark) 100%)}
  .parchment{position:absolute;left:39px;top:23px;width:798px;height:1146px;border-radius:34px;
    background:radial-gradient(ellipse at 50% 45%,var(--paper-light) 0%,var(--paper-mid) 70%,var(--paper-edge) 100%)}
  .content{position:absolute;left:0;top:0;width:873px;text-align:center}
  .brand{position:absolute;left:0;width:873px;top:63px;display:flex;flex-direction:column;align-items:center}
  .brand-mark{width:104px;height:104px;border:7px solid var(--rust);border-radius:50%}
  .brand-name{margin-top:20px;font-family:"Bungee",sans-serif;font-size:34px;line-height:38px;letter-spacing:3px;color:var(--ink)}
  .city{position:absolute;top:280px;width:873px;font-family:"Oswald",sans-serif;font-size:14px;letter-spacing:7px;color:var(--rust)}
  .facility{position:absolute;top:320px;width:873px;font-family:"Rye",serif;font-size:31px;line-height:38px;letter-spacing:2px;color:var(--rust);
    text-shadow:2px 2px 0 var(--rust-dark)}
  .why{position:absolute;top:420px;width:873px;font-family:"Anton",sans-serif;font-size:50px;line-height:64px;color:var(--rust);
    -webkit-text-stroke:1.5px var(--rust-dark)}
  .intro{position:absolute;left:118px;top:522px;width:642px;font-family:"Oswald",sans-serif;font-weight:600;font-size:10.6px;line-height:16.5px;color:var(--rust)}
  .pricing{position:absolute;left:119px;top:661px;width:648px;border:2px solid var(--rule);background:var(--green)}
  .pricing-title{height:33px;background:var(--navy);color:#fff;font-family:"Arimo",sans-serif;font-weight:700;font-size:20px;line-height:33px}
  .price-table{width:100%;border-collapse:collapse;table-layout:fixed;font-family:"Arimo",sans-serif;color:var(--ink)}
  .price-table th{height:19px;background:var(--head-row);font-size:6.5px;font-weight:700;border:1px solid var(--rule)}
  .price-table th.lead{font-size:12px}
  .price-table td{border:1px solid var(--rule);font-size:13px;vertical-align:middle}
  .price-table tr.green td{background:var(--green)}
  .price-table tr.peach td{background:var(--peach)}
  .price-table td.type{font-weight:700;font-size:13px;line-height:13px}
  .price-table td.type.small{font-size:9.5px;line-height:11px}
  .stack{display:flex;flex-direction:column;justify-content:space-around;height:84px;padding:4px 0}
  .stack.monthly{font-size:8px;font-weight:700}
  .stack.left{text-align:left;padding-left:10px}
</style>
</head>
<body>
<main class="sheet">
  <div class="parchment" role="img" aria-label="Aged parchment sheet with burnt edges on a wooden board"></div>
  <div class="content">
    <header class="brand">
      <div class="brand-mark"></div>
      <div class="brand-name">COPPERFIELD<br>YARD</div>
    </header>
    <p class="city">ALBUQUERQUE, NM</p>
    <h2 class="facility">STRENGTH AND CONDITIONING<br>FACILITY</h2>
    <h1 class="why">Why of the Copperfield Yard?</h1>
    <p class="intro">With the help of our highly skilled team of coaches and professional educators we will help you expand your strategies to develop a new you. We will teach you how and why to balance your workouts, nutrition, recovery, sleep and mental focus to become the optimal you. We incorporate an athlete centered approach, and “yes” you are an athlete. Like the great Hal Dempsey said “If you have a body, you are an athlete.” We will help you integrate a more centered approach to your health and wellness, you will be empowered to push through until you reach your goal.</p>

    <section class="pricing">
      <div class="pricing-title">Pricing for Copperfield Yard</div>
      <table class="price-table">
        <colgroup>
          <col style="width:124px"><col style="width:73px"><col style="width:74px"><col style="width:71px">
          <col style="width:78px"><col style="width:71px"><col style="width:73px"><col style="width:84px">
        </colgroup>
        <thead>
          <tr><th class="lead">Training Type</th><th>Type of Training</th><th>Sessions/week</th><th>Price/session</th><th>Monthly training price</th><th>Classes/week</th><th>Massage/Month</th><th>Massage Price</th></tr>
        </thead>
        <tbody>
          <tr class="green">
            <td class="type">Private Training</td><td>1 on 1</td>
            <td><div class="stack"><span>1</span><span>2</span><span>3</span></div></td>
            <td><div class="stack left"><span>$70.00</span><span>$65.00</span><span>$60.00</span></div></td>
            <td><div class="stack monthly"><span>$349.00</span><span>$679.00</span><span>$899.00</span></div></td>
            <td><div class="stack"><span>Unlimited</span><span>Unlimited</span><span>Unlimited</span></div></td>
            <td><div class="stack"><span>1</span><span>1</span><span>1</span></div></td>
            <td><div class="stack left"><span>$60.00</span><span>$60.00</span><span>$60.00</span></div></td>
          </tr>
          <tr class="peach">
            <td class="type">Partner Training</td><td>2 on 1</td>
            <td><div class="stack"><span>1</span><span>2</span><span>3</span></div></td>
            <td><div class="stack left"><span>$55.00</span><span>$50.00</span><span>$45.00</span></div></td>
            <td><div class="stack monthly"><span>$349.00</span><span>$549.00</span><span>$659.00</span></div></td>
            <td><div class="stack"><span>Unlimited</span><span>Unlimited</span><span>Unlimited</span></div></td>
            <td><div class="stack"><span>1</span><span>1</span><span>1</span></div></td>
            <td><div class="stack left"><span>$60.00</span><span>$60.00</span><span>$60.00</span></div></td>
          </tr>
          <tr class="green">
            <td class="type small">Small Group Training w/ Individualized plan</td><td>3 to 5</td>
            <td><div class="stack"><span>1</span><span>2</span><span>3</span></div></td>
            <td><div class="stack left"><span>$25.00</span><span>$25.00</span><span>$25.00</span></div></td>
            <td><div class="stack monthly"><span>$199.00</span><span>$299.00</span><span>$399.00</span></div></td>
            <td><div class="stack"><span>Unlimited</span><span>Unlimited</span><span>Unlimited</span></div></td>
            <td><div class="stack"><span>1</span><span>1</span><span>1</span></div></td>
            <td><div class="stack left"><span>$60.00</span><span>$60.00</span><span>$60.00</span></div></td>
          </tr>
          <tr class="peach">
            <td class="type">Class Training</td><td>4 -9</td>
            <td><div class="stack"><span>1</span><span>2</span><span>unlimited</span></div></td>
            <td><div class="stack left"><span>$15.00</span><span>$15.00</span><span>&nbsp;</span></div></td>
            <td><div class="stack monthly"><span>$89.00</span><span>$129.00</span><span>$149.00</span></div></td>
            <td><div class="stack"><span>1</span><span>2</span><span>Unlimited</span></div></td>
            <td><div class="stack"><span>0</span><span>0</span><span>0</span></div></td>
            <td><div class="stack left"><span>$60.00</span><span>$60.00</span><span>$60.00</span></div></td>
          </tr>
        </tbody>
      </table>
    </section>
  </div>
</main>
</body>
</html>
```